Business Card Design for Lawn Management

Lawn Management

Industry/Entity Type

Business

Contact Information for Business Card

Calloway Lawn Management
Joel Calloway
Calloway_Lawn@brindlemail.com
404-555-0172

```html
<!DOCTYPE html>
<html lang="en">
<head>
<meta charset="utf-8">
<title>Calloway Lawn Management — Business Card</title>
<link rel="stylesheet" href="https://fonts.googleapis.com/css2?family=Lato:wght@400;700&display=swap">
<style>
  :root {
    --stage: #1c1c1e;
    --grass-light: #4f7a2c;
    --grass-mid: #3c6420;
    --grass-dark: #2a4a15;
    --brand-green: #3f9a2e;
    --ink-dark: #141a10;
    --paper: #f7f7f5;
    --paper-shade: #dcdcd8;
    --text-light: #f2f2ee;
    --text-soft: #d8e2cf;
    --icon-fill: #e9ece5;
    --icon-ink: #5c8a3a;
  }
  * { box-sizing: border-box; margin: 0; padding: 0; }
  html, body { width: 1200px; height: 873px; overflow: hidden; }
  body {
    background: var(--stage);
    font-family: "Lato", Arial, sans-serif;
    position: relative;
  }
  .card {
    position: absolute;
    width: 560px;
    height: 320px;
    border-radius: 22px;
    overflow: hidden;
    box-shadow: 0 14px 30px rgba(0,0,0,.55);
  }
  .card--front { left: 20px; top: 276px; }
  .card--back  { left: 620px; top: 276px; }

  .grass {
    position: absolute; inset: 0;
    background:
      radial-gradient(ellipse at 35% 30%, var(--grass-light) 0%, transparent 60%),
      radial-gradient(ellipse at 75% 75%, var(--grass-mid) 0%, transparent 65%),
      linear-gradient(135deg, var(--grass-mid), var(--grass-dark));
  }

  /* front */
  .front-brand {
    position: absolute; left: 0; right: 0; top: 0; bottom: 0;
    display: flex; flex-direction: column; align-items: center; justify-content: center;
    gap: 14px;
  }
  .brand-dot { width: 62px; height: 62px; border-radius: 50%; }
  .front-brand .brand-dot { background: var(--ink-dark); }
  .brand-name {
    font-weight: 700; text-align: center; line-height: 1.1;
  }
  .front-brand .brand-name { color: var(--ink-dark); font-size: 34px; }

  /* back */
  .back-panel { position: absolute; left: 0; top: 0; width: 300px; height: 320px; }
  .back-brand {
    position: absolute; left: 18px; top: 0; width: 230px; height: 320px;
    display: flex; flex-direction: column; align-items: center; justify-content: center;
    gap: 12px;
  }
  .back-brand .brand-dot { background: var(--brand-green); width: 56px; height: 56px; }
  .back-brand .brand-name { color: var(--brand-green); font-size: 26px; }

  .contact {
    position: absolute; left: 318px; top: 62px; width: 230px; color: var(--text-light);
  }
  .contact__name { font-weight: 700; font-size: 19px; text-align: center; }
  .contact__role { font-size: 11px; color: var(--text-soft); text-align: center; margin-top: 3px; }
  .contact__list { list-style: none; margin-top: 40px; }
  .contact__item {
    display: flex; align-items: center; gap: 9px;
    font-size: 13px; margin-bottom: 13px; white-space: nowrap;
  }
  .contact__icon {
    width: 24px; height: 24px; border-radius: 50%; background: var(--icon-fill);
    display: flex; align-items: center; justify-content: center; flex: none;
  }
</style>
</head>
<body>
  <section class="card card--front" aria-label="Card front">
    <div class="grass" role="img" aria-label="Close-up of green lawn grass"></div>
    <div class="front-brand">
      <span class="brand-dot"></span>
      <p class="brand-name">Calloway<br>Lawn Management</p>
    </div>
  </section>

  <section class="card card--back" aria-label="Card back">
    <div class="grass" role="img" aria-label="Close-up of green lawn grass"></div>
    <svg class="back-panel" viewBox="0 0 300 320" aria-hidden="true">
      <path d="M0 52 C90 44 200 34 262 30 C300 120 300 230 270 320 L0 320 Z" fill="var(--paper-shade)" transform="translate(6 2)" opacity=".7"/>
      <path d="M0 52 C90 44 200 34 262 30 C300 120 300 230 270 320 L0 320 Z" fill="var(--paper)"/>
    </svg>
    <div class="back-brand">
      <span class="brand-dot"></span>
      <p class="brand-name">Calloway<br>Lawn Management</p>
    </div>
    <div class="contact">
      <p class="contact__name">Joel Calloway</p>
      <p class="contact__role">Owner / Founder</p>
      <ul class="contact__list">
        <li class="contact__item">
          <span class="contact__icon">
            <svg width="12" height="14" viewBox="0 0 12 14"><rect x="2" y="0.8" width="8" height="12.4" rx="1.5" fill="none" stroke="var(--icon-ink)" stroke-width="1.4"/><circle cx="6" cy="11" r=".8" fill="var(--icon-ink)"/></svg>
          </span>
          404-555-0172
        </li>
        <li class="contact__item">
          <span class="contact__icon">
            <svg width="14" height="10" viewBox="0 0 14 10"><rect x=".7" y=".7" width="12.6" height="8.6" fill="none" stroke="var(--icon-ink)" stroke-width="1.3"/><path d="M1 1 L7 6 L13 1" fill="none" stroke="var(--icon-ink)" stroke-width="1.3"/></svg>
          </span>
          Calloway_Lawn@brindlemail.com
        </li>
      </ul>
    </div>
  </section>
</body>
</html>
```